Flyer Template

I need a flyer template for door knocking on properties. Text Boxes need to be editable, with a header and text body. Footer to be my info. Project to be stylized to match my real estate signs and logo art from past projects

```html
<!DOCTYPE html>
<html lang="en">
<head>
<meta charset="utf-8">
<title>House For Sale Flyer</title>
<link href="https://fonts.googleapis.com/css2?family=Open+Sans:wght@400;600;700;800&display=swap" rel="stylesheet">
<style>
  :root{
    --red:#e2261f;
    --dark:#2a2a2a;
    --slate:#3d3d3d;
    --ink:#444444;
    --white:#ffffff;
    --page:#e4e4e4;
    --avatar:#d9dadb;
  }
  *{box-sizing:border-box;margin:0;padding:0}
  html,body{width:1200px;height:1200px;overflow:hidden;background:var(--page);font-family:"Open Sans",Arial,sans-serif}
  .flyer{position:absolute;left:150px;top:18px;width:900px;height:1164px;background:var(--white);overflow:hidden}

  .hero-photo{position:absolute;left:0;top:0;width:900px;height:534px;
    background:
      linear-gradient(180deg,rgba(255,255,255,0) 78%,#6d9a45 90%,#5f8c3a 100%),
      linear-gradient(90deg,#dfe5e8 0%,#c9d2d6 30%,#b5b6bb 55%,#8e8a93 72%,#9aa4b3 100%),
      linear-gradient(180deg,#f4f7fa 0%,#c9dcee 35%,#a8bfd6 55%,rgba(0,0,0,0) 56%);
    background-blend-mode:normal}
  .hero-photo .sky{position:absolute;left:0;top:0;width:900px;height:300px;
    background:linear-gradient(180deg,#ffffff 0%,#eaf1f8 35%,#bcd3ea 100%)}
  .hero-photo .scene{position:absolute;left:0;top:240px;width:900px;height:294px;
    background:linear-gradient(90deg,#55784a 0%,#e9ecef 18%,#cfd3d6 40%,#a19a96 62%,#7b7580 78%,#8fa0b5 100%)}
  .hero-photo .lawn{position:absolute;left:0;top:440px;width:900px;height:94px;
    background:linear-gradient(180deg,#b4aa98 0%,#8f9a6d 45%,#62923d 100%)}
  .hero-photo::after{content:"";position:absolute;left:0;top:0;width:560px;height:170px;
    background:linear-gradient(90deg,#ffffff 45%,rgba(255,255,255,0) 100%)}

  .brand{position:absolute;left:56px;top:64px;display:flex;align-items:center;gap:22px;z-index:2}
  .brand-mark{width:58px;height:58px;background:var(--red)}
  .brand-name{font-weight:800;font-size:30px;color:#1e1e1e;letter-spacing:.2px}

  .title-band{position:absolute;left:0;top:162px;width:550px;height:72px;background:var(--dark);
    display:flex;align-items:center;padding-left:40px}
  .title-band h1{font-weight:800;font-size:47px;color:var(--white);letter-spacing:.5px}
  .title-band h1 span{color:var(--red)}

  .description{position:absolute;left:42px;top:574px;font-size:14.6px;line-height:20px;color:var(--ink);white-space:nowrap}

  .features-tab{position:absolute;left:0;top:750px;width:306px;height:38px}
  .features-tab svg{position:absolute;inset:0}
  .features-tab h2{position:relative;font-weight:700;font-size:19.5px;color:var(--white);line-height:38px;padding-left:41px;letter-spacing:.3px}
  .feature-list{position:absolute;left:49px;top:802px;list-style:none}
  .feature-list li{display:flex;align-items:center;gap:12px;height:29px;font-size:14.6px;color:var(--ink)}
  .feature-list svg{width:15px;height:15px;flex:none}

  .room-photo{position:absolute;left:496px;width:389px;height:215px}
  .room-bedroom{top:573px;background:linear-gradient(180deg,#9fb9bf 0%,#b8c8ca 40%,#e2ded6 62%,#d8d3c9 80%,#8b6e52 100%)}
  .room-kitchen{top:797px;background:linear-gradient(180deg,#f2f2f0 0%,#dcdcda 40%,#9a9c9e 58%,#e7e7e6 72%,#7a5236 100%)}
  .price-tag{position:absolute;left:567px;top:768px;width:248px;height:50px;background:var(--red);
    color:var(--white);font-weight:700;font-size:33px;text-align:center;line-height:50px}

  .footer-shapes{position:absolute;left:0;top:1034px}
  .agent-photo{position:absolute;left:42px;top:983px;width:154px;height:146px;background:var(--white);padding:6px}
  .agent-photo div{width:100%;height:100%;background:var(--avatar)}
  .agent-name{position:absolute;left:222px;top:1040px;font-weight:700;font-size:19.5px;color:var(--white);letter-spacing:.3px}
  .agent-contact{position:absolute;left:222px;top:1077px;list-style:none}
  .agent-contact li{display:flex;align-items:center;gap:12px;height:27px;font-size:19px;color:var(--white)}
  .agent-contact b{font-weight:700}
  .agent-contact svg{width:22px;height:22px;flex:none}

  .partner{position:absolute;left:590px;top:1064px;width:287px;height:71px;border:1px solid #4d4d4d;
    display:flex;align-items:center;justify-content:center}
  .partner span{font-weight:700;font-size:24px;color:var(--white);letter-spacing:.5px}
</style>
</head>
<body>
<main class="flyer">
  <div class="hero-photo" role="img" aria-label="Photo of a modern two-storey house with carport and lawn under a blue sky">
    <div class="sky"></div>
    <div class="scene"></div>
    <div class="lawn"></div>
  </div>

  <header class="brand">
    <div class="brand-mark"></div>
    <div class="brand-name">MARWOOD REALTY</div>
  </header>

  <div class="title-band"><h1>HOUSE <span>FOR SALE</span></h1></div>

  <p class="description">Lorem ipsum dolor sit amet, consectetur adipiscing elit.<br>Vivamus ac dolor vel sem luctus condimentum. In at finibus<br>massa. In congue risus lacinia libero dignissim, ac cursus<br>neque luctus. Curabitur tempor tellus eros, et ornare eros<br>aliquam sit amet. Vestibulum auctor nunc ut odio accumsan<br>fermentum. Aenean sed nulla nisl. Etiam at turpis sit amet<br>felis gravida tincidunt sed vitae leo.</p>

  <div class="features-tab">
    <svg width="306" height="38" viewBox="0 0 306 38"><polygon points="0,0 268,0 306,38 0,38" fill="var(--red)"/></svg>
    <h2>PROPERTY FEATURES</h2>
  </div>

  <ul class="feature-list">
    <li><svg viewBox="0 0 16 16"><circle cx="8" cy="8" r="6.5" fill="none" stroke="var(--red)" stroke-width="1.6"/><path d="M5 8.2l2.2 2.2L13.5 4" fill="none" stroke="var(--red)" stroke-width="1.8"/></svg>Lorem ipsum dolor sit amet.</li>
    <li><svg viewBox="0 0 16 16"><circle cx="8" cy="8" r="6.5" fill="none" stroke="var(--red)" stroke-width="1.6"/><path d="M5 8.2l2.2 2.2L13.5 4" fill="none" stroke="var(--red)" stroke-width="1.8"/></svg>Vivamus ac dolor vel sem luctus condimentum.</li>
    <li><svg viewBox="0 0 16 16"><circle cx="8" cy="8" r="6.5" fill="none" stroke="var(--red)" stroke-width="1.6"/><path d="M5 8.2l2.2 2.2L13.5 4" fill="none" stroke="var(--red)" stroke-width="1.8"/></svg>In congue risus lacinia libero dignissim.</li>
    <li><svg viewBox="0 0 16 16"><circle cx="8" cy="8" r="6.5" fill="none" stroke="var(--red)" stroke-width="1.6"/><path d="M5 8.2l2.2 2.2L13.5 4" fill="none" stroke="var(--red)" stroke-width="1.8"/></svg>Etiam at turpis sit amet felis.</li>
    <li><svg viewBox="0 0 16 16"><circle cx="8" cy="8" r="6.5" fill="none" stroke="var(--red)" stroke-width="1.6"/><path d="M5 8.2l2.2 2.2L13.5 4" fill="none" stroke="var(--red)" stroke-width="1.8"/></svg>Aenean sed nulla nisl.</li>
  </ul>

  <div class="room-photo room-bedroom" role="img" aria-label="Photo of a bright bedroom with a made bed and bedside lamps"></div>
  <div class="room-photo room-kitchen" role="img" aria-label="Photo of a white modern kitchen with island and bar stools"></div>
  <div class="price-tag">$3000,000</div>

  <svg class="footer-shapes" width="900" height="130" viewBox="0 0 900 130">
    <rect x="0" y="36" width="900" height="94" fill="var(--dark)"/>
    <polygon points="490,15 900,15 900,130 595,130" fill="var(--slate)"/>
    <polygon points="197,0 473,0 505,36 197,36" fill="var(--red)"/>
    <rect x="0" y="0" width="42" height="35" fill="var(--red)"/>
  </svg>

  <div class="agent-photo" role="img" aria-label="Agent portrait placeholder"><div></div></div>
  <div class="agent-name">JORDAN MARWOOD</div>
  <ul class="agent-contact">
    <li><svg viewBox="0 0 24 24"><circle cx="12" cy="12" r="10.5" fill="none" stroke="var(--white)" stroke-width="1.5"/><path d="M8.5 7h2l1 2.6-1.3 1a6 6 0 0 0 3.2 3.2l1-1.3 2.6 1v2a1 1 0 0 1-1 1A8.5 8.5 0 0 1 7.5 8a1 1 0 0 1 1-1z" fill="var(--red)"/></svg><b>907-555-0148</b></li>
    <li><svg viewBox="0 0 24 24"><circle cx="12" cy="12" r="10.5" fill="none" stroke="var(--white)" stroke-width="1.5"/><rect x="6.5" y="8" width="11" height="8" rx="1" fill="var(--red)"/><path d="M6.8 8.5l5.2 4 5.2-4" fill="none" stroke="var(--white)" stroke-width="1"/></svg><span><b>jmarwood</b>@mailbox.com</span></li>
  </ul>

  <div class="partner"><span>NORTHLINE GROUP</span></div>
</main>
</body>
</html>
```